Wolkenfeld - a property developer - Website design

Hi all!
Exciting new project for you! :)
We are looking for some creative/modern designs to best represent us as a company.
Please have a look at the following link: huhu.wolkenfeld.eu to get an idea about who we are and what we do.
The 'Main Page' of the HP should be neatly arranged, easy to navigate, contain several pictures (changing every 10 seconds or so) that should reflect that we are property developers.
The navigation points ('About us', 'Projects' 'Investment', 'Contact Us', 'Legal Notice') should be included in the Design (again under every navigation point, pictures may be added - that reflect our profession and/or the subsection)
What we will need at the end of the day is a fully functional site - i.e: a site that is designed and programmed with backend/wordpress, to allow us to make changes anytime we feel like it.
Further questions?! Don't hesitate to contact me! Thanks :)
Target Market(s)
Real Estate Development/Building sector
Industry/Entity Type
Real Estate Development
Number of Pages Required
5+ page
Look and feel

```html
<!DOCTYPE html>
<html lang="en">
<head>
<meta charset="utf-8">
<title>Wolkenfeld – Property Developer</title>
<link href="https://fonts.googleapis.com/css2?family=Open+Sans:ital,wght@0,300;0,400;0,600;0,700;1,400&display=swap" rel="stylesheet">
<style>
:root{
  --ink:#333;
  --text:#555;
  --muted:#777;
  --white:#fff;
  --accent:#f39c12;
  --accent-dark:#e08a00;
  --band:#e9e9e9;
  --footer:#2b2b2b;
  --footer-bottom:#1f1f1f;
  --footer-text:#aaa;
  --dot:#c8c8c8;
}
*{margin:0;padding:0;box-sizing:border-box}
html,body{width:1200px;height:2179px;overflow:hidden}
body{position:relative;background:var(--white);font-family:"Open Sans",Arial,sans-serif;color:var(--text)}
.abs{position:absolute}

/* header */
.site-header{position:absolute;left:0;top:0;width:1200px;height:78px;background:var(--white)}
.brand{position:absolute;left:99px;top:18px;display:flex;align-items:center;gap:10px}
.brand-square{width:22px;height:40px;background:var(--ink)}
.brand-name{font-size:30px;font-weight:700;color:var(--ink);letter-spacing:1px;text-transform:uppercase}
.main-nav a{position:absolute;top:32px;font-size:13px;font-weight:600;color:var(--ink);text-decoration:none;text-transform:uppercase}
.lang-select{position:absolute;left:991px;top:26px;width:110px;height:28px;border:1px solid #ccc;border-radius:3px;font-size:12px;color:var(--text);display:flex;align-items:center;padding-left:10px;gap:8px}
.lang-flag{width:16px;height:11px;background:#2a4a8c;border:1px solid #b33}
.lang-caret{margin-left:auto;margin-right:10px;font-size:10px}

/* hero */
.hero{position:absolute;left:0;top:78px;width:1200px;height:464px;
  background:linear-gradient(180deg,#14244a 0%,#2c3d62 38%,#4d5446 60%,#5a4b3c 70%,#1fa6d8 80%,#0f6f9a 100%)}
.hero-title{position:absolute;left:0;top:202px;width:1200px;text-align:center;color:var(--white);font-size:38px;font-weight:700;text-transform:uppercase;text-shadow:0 2px 4px rgba(0,0,0,.4)}
.hero-sub{position:absolute;left:0;top:250px;width:1200px;text-align:center;color:var(--white);font-size:22px;font-weight:300;text-transform:uppercase}
.hero-arrow{position:absolute;top:200px}

/* sections */
.section-title{position:absolute;left:0;width:1200px;text-align:center;font-size:20px;font-weight:600;color:var(--ink);text-transform:uppercase}
.section-text{position:absolute;left:150px;width:900px;text-align:center;font-size:12px;line-height:27px;color:var(--text)}

.invest-title{position:absolute;left:400px;top:780px;width:242px;text-align:right;font-size:21px;font-weight:600;color:var(--ink);text-transform:uppercase}
.invest-text{position:absolute;left:140px;top:820px;width:502px;text-align:right;font-size:11px;line-height:25px;color:var(--text)}
.btn-more{position:absolute;left:506px;top:934px;width:136px;height:38px;background:var(--accent);border-bottom:2px solid var(--accent-dark);color:var(--white);font-size:11px;font-weight:700;text-transform:uppercase;display:flex;align-items:center;justify-content:center;border-radius:2px}
.invest-photo{position:absolute;left:702px;top:784px;width:399px;height:185px;background:linear-gradient(90deg,#d9d9d9,#b9a696 45%,#e4e4e4)}

.subline{position:absolute;left:0;width:1200px;text-align:center;font-size:11px;color:var(--text);text-transform:uppercase}
.project-card{position:absolute;top:1145px;width:225px}
.project-photo{width:225px;height:145px}
.project-caption{margin-top:16px;text-align:center;font-size:12px;font-weight:700;color:var(--ink);text-transform:uppercase}

.dots{position:absolute;left:581px;display:flex;gap:7px}
.dots span{width:8px;height:8px;border-radius:50%;background:var(--dot)}
.dots span.active{background:var(--accent)}

/* news */
.news-band{position:absolute;left:0;top:1437px;width:1200px;height:402px;background:var(--band)}
.news-item{position:absolute;top:1614px}
.news-photo{position:absolute;left:0;top:0;width:167px;height:118px}
.news-body{position:absolute;left:197px;top:8px;width:270px}
.news-title{font-size:12px;font-weight:700;line-height:22px;color:var(--ink);text-transform:uppercase}
.news-date{margin-top:3px;font-size:11px;color:var(--text);display:flex;align-items:center;gap:6px}
.news-excerpt{margin-top:6px;font-size:11px;line-height:23px;color:var(--text)}

/* footer */
.site-footer{position:absolute;left:0;top:1839px;width:1200px;height:289px;background:var(--footer)}
.footer-bottom{position:absolute;left:0;top:2128px;width:1200px;height:51px;background:var(--footer-bottom);color:var(--footer-text);font-size:11px;text-align:center;line-height:51px}
.footer-heading{position:absolute;top:1880px;font-size:12px;font-weight:700;color:var(--white);text-transform:uppercase}
.footer-links{position:absolute;top:1908px;list-style:none;font-size:11px;line-height:22px;color:var(--footer-text)}
.quote{position:absolute;left:130px;top:1922px;width:265px;font-size:10px;font-style:italic;line-height:20.5px;color:var(--footer-text)}
.quote-mark{position:absolute;font-size:26px;color:#666;font-family:Georgia,serif}
.avatar{position:absolute;left:126px;top:2045px;width:50px;height:50px;border-radius:50%;background:linear-gradient(#e9e4df,#c9c2bb);border:2px solid var(--white)}
.person-name{position:absolute;left:186px;top:2053px;font-size:11px;font-weight:700;color:var(--white);text-transform:uppercase}
.person-role{position:absolute;left:186px;top:2072px;font-size:12px;color:#888}
.social{position:absolute;left:936px;display:flex;align-items:center;gap:8px;font-size:11px;color:var(--footer-text)}
.social-dot{width:27px;height:27px;border-radius:50%;background:#555}
.testi-nav{position:absolute;left:370px;top:1878px;color:#bbb;font-size:13px;letter-spacing:6px}
</style>
</head>
<body>

<header class="site-header">
  <div class="brand"><span class="brand-square"></span><span class="brand-name">Wolkenfeld</span></div>
  <nav class="main-nav">
    <a style="left:359px">Home</a>
    <a style="left:439px">About us</a>
    <a style="left:543px">Projects</a>
    <a style="left:643px">Investment</a>
    <a style="left:764px">Contact us</a>
    <a style="left:883px">Legal notice</a>
  </nav>
  <div class="lang-select"><span class="lang-flag"></span>English<span class="lang-caret">&#8964;</span></div>
</header>

<section class="hero" role="img" aria-label="Modern timber villa at night with illuminated pool and loungers">
  <svg class="hero-arrow" style="left:36px" width="30" height="30" viewBox="0 0 30 30"><circle cx="15" cy="15" r="14" fill="rgba(255,255,255,.25)"/><path d="M17 9l-6 6 6 6" stroke="#fff" stroke-width="2" fill="none"/></svg>
  <svg class="hero-arrow" style="left:1134px" width="30" height="30" viewBox="0 0 30 30"><circle cx="15" cy="15" r="14" fill="rgba(255,255,255,.25)"/><path d="M13 9l6 6-6 6" stroke="#fff" stroke-width="2" fill="none"/></svg>
  <h1 class="hero-title">Build up on a safe investment</h1>
  <p class="hero-sub">Lindenhaldeweg - Townhouse - Completed</p>
</section>

<h2 class="section-title" style="top:603px">Quality, skills and experience: everything under one roof</h2>
<p class="section-text" style="top:648px">Wolkenfeld is a combination of potent companies pursuing a common goal: the realization of modern, sustainable housing projects for highest demands in Vienna. Our building companies' efforts are concentrating on the two core areas of new developments and roof extensions.</p>

<h2 class="invest-title">Investment</h2>
<p class="invest-text">Lorem Ipsum is simply dummy text of the printing and typesetting industry. Lorem Ipsum has been the industry's standard dummy text ever since the 1500s, when an unknown printer took a galley of type and scrambled it to make a type specimen book. It has survived not only five centuries, but also the leap into electronic typesetting...</p>
<div class="btn-more">Read more info</div>
<div class="invest-photo" role="img" aria-label="Group of business people in suits"></div>

<h2 class="section-title" style="top:1049px">Projects</h2>
<p class="subline" style="top:1093px">Lindenhaldeweg - Townhouse - Completed</p>

<div class="project-card" style="left:99px"><div class="project-photo" role="img" aria-label="Row of townhouses under blue sky" style="background:linear-gradient(#3f8fe0 0%,#8cc0ee 45%,#d8d2c4 60%,#6f9a3a 100%)"></div><p class="project-caption">Lorem ipsum is simply</p></div>
<div class="project-card" style="left:358px"><div class="project-photo" role="img" aria-label="Townhouse facade with timber cladding" style="background:linear-gradient(90deg,#6aa6e8,#d9d6cc 45%,#b98a4e)"></div><p class="project-caption">Lorem ipsum is simply</p></div>
<div class="project-card" style="left:617px"><div class="project-photo" role="img" aria-label="White apartment building at dusk" style="background:linear-gradient(#3d5a8c 0%,#8fa4c4 40%,#e4ddc9 65%,#4a4a3a 100%)"></div><p class="project-caption">Lorem ipsum is simply</p></div>
<div class="project-card" style="left:876px"><div class="project-photo" role="img" aria-label="House entrance with white garage door" style="background:linear-gradient(90deg,#6a5a4e,#ececec 40%,#c9c9c9 70%,#5c4a3f)"></div><p class="project-caption">Lorem ipsum is simply</p></div>

<div class="dots" style="top:1366px"><span class="active"></span><span></span><span></span></div>

<section class="news-band"></section>
<h2 class="section-title" style="top:1491px">Latest news</h2>
<p class="section-text" style="top:1534px;font-size:12px">Lorem Ipsum is simply dummy text of the printing and typesetting industry. Lorem Ipsum has been the industry's standard...</p>

<article class="news-item" style="left:99px">
  <div class="news-photo" role="img" aria-label="Businessman leaping between two tall blocks" style="background:linear-gradient(90deg,#9a9a9a,#e6e6e6 50%,#8a8a8a)"></div>
  <div class="news-body">
    <h3 class="news-title">Lorem ipsum is simply dummy text of the printing</h3>
    <p class="news-date"><svg width="11" height="11" viewBox="0 0 11 11"><rect x="0.5" y="1.5" width="10" height="9" fill="none" stroke="#888"/><line x1="0.5" y1="4" x2="10.5" y2="4" stroke="#888"/></svg>Posted on 27 March 2015</p>
    <p class="news-excerpt">Lorem Ipsum is simply dummy text of the printing and typesetting industry...</p>
  </div>
</article>
<article class="news-item" style="left:641px">
  <div class="news-photo" role="img" aria-label="Business handshake" style="background:linear-gradient(90deg,#f4e6cc,#c79a62 55%,#f6ecd9)"></div>
  <div class="news-body">
    <h3 class="news-title">Lorem ipsum is simply dummy text of the printing</h3>
    <p class="news-date"><svg width="11" height="11" viewBox="0 0 11 11"><rect x="0.5" y="1.5" width="10" height="9" fill="none" stroke="#888"/><line x1="0.5" y1="4" x2="10.5" y2="4" stroke="#888"/></svg>Posted on 27 March 2015</p>
    <p class="news-excerpt">Lorem Ipsum is simply dummy text of the printing and typesetting industry...</p>
  </div>
</article>

<div class="dots" style="top:1771px"><span class="active"></span><span></span><span></span></div>

<footer class="site-footer"></footer>
<h4 class="footer-heading" style="left:108px">Testimonials</h4>
<span class="testi-nav">&lsaquo;&rsaquo;</span>
<span class="quote-mark" style="left:105px;top:1908px">&ldquo;</span>
<p class="quote">Simply dummy text of the printing and typesetting industry. Lorem Ipsum has been the industry's standard dummy text ever since the 1500s, when an unknown printer took a galley of type and scrambled it to make a type specimen book...</p>
<span class="quote-mark" style="left:378px;top:2008px">&rdquo;</span>
<div class="avatar" role="img" aria-label="Portrait of client"></div>
<p class="person-name">Marten Colby</p>
<p class="person-role">Business man</p>

<h4 class="footer-heading" style="left:514px">Welcome</h4>
<ul class="footer-links" style="left:514px"><li>Home</li><li>About us</li><li>Projects</li><li>Investment</li><li>Contact us</li><li>Legal Notice.</li></ul>

<h4 class="footer-heading" style="left:709px">Information</h4>
<ul class="footer-links" style="left:709px"><li>Privacy Policy</li><li>Terms &amp; Conditions</li><li>Sitemap</li></ul>

<h4 class="footer-heading" style="left:936px">Follow us</h4>
<div class="social" style="top:1910px"><span class="social-dot"></span>: Friendnet</div>
<div class="social" style="top:1950px"><span class="social-dot"></span>: Chirpline</div>
<div class="social" style="top:1993px"><span class="social-dot"></span>: Workgrid</div>
<div class="social" style="top:2035px"><span class="social-dot"></span>: Searchplus</div>

<div class="footer-bottom">&copy; 2015. Wolkenfeld. All rights reserved.</div>

</body>
</html>
```